mapleridgegroup Business Card Design

Business card with logo design for mapleridgegroup. We are a group of professional project managers based on the Pareto Principle that 80% of the work is done by 20% of the people. I have a makeshift logo that uses a pi chart with 30% and 20% and the 20% pie slice is set slightly out and up. Have played around with a teal and orange colour scheme.

Industry/Entity Type

Business

Contact Information for Business Card

Gareth Pembroke
Director
mapleridgegroup

0452 803716

```html
<!DOCTYPE html>
<html lang="en">
<head>
<meta charset="utf-8">
<title>mapleridgegroup Business Card</title>
<link rel="stylesheet" href="https://fonts.googleapis.com/css2?family=Open+Sans:wght@400;600;700&display=swap">
<style>
  :root {
    --backdrop: #e9e6e2;
    --card-white: #ffffff;
    --orange-deep: #e2412f;
    --orange-light: #ee6f48;
    --teal: #1e8a98;
    --ink: #4a4a4a;
    --on-orange: #ffffff;
  }
  html, body {
    margin: 0;
    padding: 0;
    width: 1200px;
    height: 899px;
    overflow: hidden;
    background: var(--backdrop);
    font-family: "Open Sans", Arial, sans-serif;
  }
  .canvas {
    position: relative;
    width: 1200px;
    height: 899px;
  }
  .card {
    position: absolute;
    left: 250px;
    width: 700px;
    height: 400px;
    background: var(--card-white);
    box-shadow: 0 6px 18px rgba(0,0,0,0.18);
    overflow: hidden;
  }
  .card-front { top: 34px; }
  .card-back { top: 464px; }

  .brand {
    position: absolute;
    display: flex;
    align-items: center;
    gap: 14px;
  }
  .brand-dot {
    width: 46px;
    height: 46px;
    border-radius: 50%;
    background: var(--orange-light);
  }
  .brand-name {
    font-size: 34px;
    font-weight: 600;
    color: var(--teal);
    letter-spacing: 0.5px;
  }
  .card-front .brand {
    left: 50%;
    top: 50%;
    transform: translate(-50%, -50%);
  }
  .card-back .brand {
    right: 40px;
    top: 150px;
  }
  .card-back .brand-dot { width: 36px; height: 36px; }
  .card-back .brand-name { font-size: 26px; }

  .wave { position: absolute; inset: 0; }

  .holder {
    position: absolute;
    left: 36px;
    top: 44px;
    color: var(--on-orange);
  }
  .holder-name {
    margin: 0;
    font-size: 24px;
    font-weight: 700;
  }
  .holder-title {
    margin: 4px 0 0;
    font-size: 17px;
    font-weight: 400;
  }

  .contact {
    position: absolute;
    left: 36px;
    bottom: 30px;
    margin: 0;
    padding: 0;
    list-style: none;
    color: var(--on-orange);
    font-size: 13px;
    line-height: 21px;
  }
  .contact li {
    display: flex;
    align-items: flex-start;
    gap: 8px;
  }
  .contact-icon {
    flex: 0 0 14px;
    width: 14px;
    height: 14px;
    margin-top: 4px;
  }
  .contact .address { line-height: 18px; margin-bottom: 6px; }
</style>
</head>
<body>
<main class="canvas">

  <section class="card card-front" aria-label="Card front">
    <div class="brand">
      <span class="brand-dot"></span>
      <span class="brand-name">mapleridgegroup</span>
    </div>
  </section>

  <section class="card card-back" aria-label="Card back">
    <svg class="wave" viewBox="0 0 700 400" width="700" height="400" aria-hidden="true">
      <defs>
        <radialGradient id="orangeGlow" cx="0.35" cy="0.45" r="0.7">
          <stop offset="0" stop-color="var(--orange-deep)"/>
          <stop offset="1" stop-color="var(--orange-light)"/>
        </radialGradient>
      </defs>
      <path d="M0 0 H375 C335 70 320 150 385 230 C435 290 470 350 440 400 H0 Z" fill="url(#orangeGlow)"/>
      <path d="M392 0 C352 70 345 150 410 232 C455 290 482 345 455 400 L462 400 C492 345 470 285 425 230 C365 155 372 70 410 0 Z" fill="var(--teal)"/>
    </svg>

    <div class="holder">
      <h1 class="holder-name">Gareth Pembroke</h1>
      <p class="holder-title">Owner / C.E.O</p>
    </div>

    <ul class="contact">
      <li class="address">
        <svg class="contact-icon" viewBox="0 0 14 14"><circle cx="7" cy="7" r="7" fill="#fff"/><path d="M7 3 C5 3 4 4.4 4 5.8 C4 7.8 7 11 7 11 C7 11 10 7.8 10 5.8 C10 4.4 9 3 7 3Z" fill="var(--orange-light)"/></svg>
        <span>Level 4, 18 Harbour Lane,<br>NSW 2000</span>
      </li>
      <li>
        <svg class="contact-icon" viewBox="0 0 14 14"><circle cx="7" cy="7" r="7" fill="#fff"/><path d="M4.5 3.5 L6 3.5 L6.6 5.4 L5.7 6.2 C6.2 7.3 6.9 8 8 8.5 L8.8 7.6 L10.5 8.2 L10.5 9.7 C7 10 4.2 7.2 4.5 3.5Z" fill="var(--orange-light)"/></svg>
        <span>0452 803716</span>
      </li>
      <li>
        <svg class="contact-icon" viewBox="0 0 14 14"><circle cx="7" cy="7" r="7" fill="#fff"/><rect x="5" y="3" width="4" height="8" rx="1" fill="var(--orange-light)"/></svg>
        <span>0452 803717</span>
      </li>
      <li>
        <svg class="contact-icon" viewBox="0 0 14 14"><circle cx="7" cy="7" r="7" fill="#fff"/><rect x="4" y="5" width="6" height="5" fill="var(--orange-light)"/><rect x="5" y="3" width="4" height="2" fill="var(--orange-light)"/></svg>
        <span>0452 803718</span>
      </li>
      <li>
        <svg class="contact-icon" viewBox="0 0 14 14"><circle cx="7" cy="7" r="7" fill="#fff"/><rect x="3.5" y="4.5" width="7" height="5" fill="var(--orange-light)"/><path d="M3.5 4.5 L7 7.3 L10.5 4.5" stroke="#fff" stroke-width="0.8" fill="none"/></svg>
        <span>gareth@mapleridgegroup.com</span>
      </li>
      <li>
        <svg class="contact-icon" viewBox="0 0 14 14"><circle cx="7" cy="7" r="7" fill="#fff"/><circle cx="7" cy="7" r="3.6" stroke="var(--orange-light)" stroke-width="1.2" fill="none"/><path d="M3.4 7 H10.6 M7 3.4 V10.6" stroke="var(--orange-light)" stroke-width="0.8"/></svg>
        <span>www.mapleridgegroup.com</span>
      </li>
    </ul>

    <div class="brand">
      <span class="brand-dot"></span>
      <span class="brand-name">mapleridgegroup</span>
    </div>
  </section>

</main>
</body>
</html>
```